Business Card Design Project

I want a cleaner business card and envelope then what we have now, its too crowded.
Updates

I update with logo, this can be changed anyway you feel it looks best. I also have put gaurantee on there and extended time, this is my first time doing this. Also gave an example of current card

Target Market(s)

a wide array of customers from lattice 700 to small companies and cleints

Industry/Entity Type

Business

Requirements
Must have
• Need to have address, telephone number email
Nice to have
• a sharp professional card that stands out but is still very clean.
Should not have
• Not crazy looking

```html
<!DOCTYPE html>
<html lang="en">
<head>
<meta charset="utf-8">
<title>Harborline Insurance Group – Business Card</title>
<link href="https://fonts.googleapis.com/css2?family=Questrial&family=Open+Sans:wght@400&display=swap" rel="stylesheet">
<style>
  :root {
    --backdrop: #5a5a5a;
    --card: #ffffff;
    --band: #f1f1f1;
    --band-deep: #dcdcdc;
    --swirl: #e4e4e4;
    --sheen-edge: #dedede;
    --ink: #2e2e2e;
    --ink-soft: #5a5a5a;
    --label: #6f6f6f;
    --mark: #8a8a8a;
  }
  * { margin: 0; padding: 0; box-sizing: border-box; }
  html, body { width: 1200px; height: 517px; overflow: hidden; background: var(--backdrop); }
  body { position: relative; font-family: "Open Sans", sans-serif; color: var(--ink); }

  .card { position: absolute; top: 100px; width: 493px; height: 285px; background: var(--card); overflow: hidden; }
  .card--front { left: 45px; }
  .card--back { left: 595px; }

  .card-art { position: absolute; inset: 0; width: 100%; height: 100%; }
  .back-sheen { position: absolute; inset: 0;
    background: radial-gradient(ellipse 62% 72% at 52% 38%, #ffffff 62%, var(--sheen-edge) 100%); }

  .front-header { position: absolute; left: 0; top: 0; width: 100%; height: 80px;
    background: linear-gradient(90deg, var(--band) 0%, #fafafa 60%, #ffffff 100%); }
  .holder-name { position: absolute; left: 14px; top: 11px; font-family: "Questrial", sans-serif;
    font-weight: 400; font-size: 28px; font-variant: small-caps; letter-spacing: 0.3px; color: var(--ink-soft); }
  .holder-role { position: absolute; left: 167px; top: 51px; font-size: 12.5px; color: var(--ink-soft); }

  .brand-small { position: absolute; left: 396px; top: 12px; width: 90px; text-align: center; }
  .brand-small .brand-square { width: 30px; height: 30px; margin: 0 auto 3px; background: var(--mark); }
  .brand-small .brand-name { font-family: "Questrial", sans-serif; color: var(--ink); font-size: 11px; letter-spacing: 1px; line-height: 1; }
  .brand-small .brand-sub { font-family: "Questrial", sans-serif; color: var(--ink); font-size: 5.5px; letter-spacing: 0.6px; line-height: 1.3; }

  .contact { position: absolute; left: 0; font-size: 12.5px; line-height: 19px; }
  .contact dt { position: absolute; width: 64px; text-align: right; font-size: 10.5px; color: var(--label); }
  .contact dd { margin-left: 73px; color: var(--ink); }
  .contact--address { top: 94px; }
  .contact--phones { top: 150px; }
  .contact--email { top: 252px; }
  .contact--email dd { font-size: 13px; }

  .brand-large { position: absolute; left: 0; top: 62px; width: 100%; text-align: center; }
  .brand-large .brand-square { width: 78px; height: 78px; margin: 0 auto 10px; background: var(--mark); }
  .brand-large .brand-name { font-family: "Questrial", sans-serif; color: var(--ink); font-size: 30px; letter-spacing: 3px; line-height: 1; }
  .brand-large .brand-sub { font-family: "Questrial", sans-serif; color: var(--ink); font-size: 14px; letter-spacing: 2px; line-height: 1.4; }
  .web { position: absolute; left: 0; top: 243px; width: 100%; text-align: center; font-size: 12.5px; color: var(--ink); }
</style>
</head>
<body>

<section class="card card--front" aria-label="Business card front">
  <div class="front-header"></div>
  <svg class="card-art" viewBox="0 0 493 285" aria-hidden="true">
    <path d="M0 224 C150 210 330 206 493 216 L493 285 L0 285 Z" fill="var(--swirl)"/>
    <path d="M0 240 C160 222 340 224 493 236 L493 285 L0 285 Z" fill="var(--band-deep)"/>
    <path d="M0 232 C150 218 330 214 493 226" fill="none" stroke="#ffffff" stroke-width="4"/>
  </svg>
  <h1 class="holder-name">Marla Quinn - Hayes</h1>
  <p class="holder-role">Operations Manager</p>
  <div class="brand-small">
    <div class="brand-square"></div>
    <div class="brand-name">HARBORLINE</div>
    <div class="brand-sub">INSURANCE GROUP</div>
  </div>
  <dl class="contact contact--address">
    <dt>Address :</dt><dd>18230 Orchard Row<br>Maple Ridge, MI 48000</dd>
  </dl>
  <dl class="contact contact--phones">
    <dt>Phone :</dt><dd>555 - 214 - 3300 ext 214</dd>
    <dt>Direct :</dt><dd>555 - 481 - 0927</dd>
    <dt>Fax :</dt><dd>555 - 214 - 3301</dd>
  </dl>
  <dl class="contact contact--email">
    <dt>E - mail :</dt><dd>mquinn-hayes@harborlineagency.com</dd>
  </dl>
</section>

<section class="card card--back" aria-label="Business card back">
  <div class="back-sheen" role="img" aria-label="Soft grey flowing ribbon backdrop"></div>
  <div class="brand-large">
    <div class="brand-square"></div>
    <div class="brand-name">HARBORLINE</div>
    <div class="brand-sub">INSURANCE GROUP</div>
  </div>
  <p class="web">www.harborlineagency.com</p>
</section>

</body>
</html>
```